Roll-Up Banner für Glückswebsite
Zielgruppe
Die Website, www.heiterkompass.de ermöglicht es jedem Interessierten kostenlos mehr über das eigene Lebensglück, persönliche Stärken, und die eigene Lebenszufriedenheit herauszufinden. Interessierte können online Fragebögen ausfüllen, und erhalten neben einer detaillierten Rückmeldung über die eigenen Möglichkeiten und Stärken, Hinweise dazu, wie Sie an Ihrem eigenen Potenzial arbeiten können. Es handelt sich um ein Kooperationsprojekt der Nordischen Vereinigung für Angewandte Seelenkunde der Uni Wolkenrode, der HK-Selmhorst, der Medical School Trebnitz und der Uni Kalbenau. Zielgruppe für das Banner sind Menschen, die selbst mit Klienten im Kontext der Positiven Psychologie arbeiten oder Menschen, die sich Ihrem eigenen Lebensglück zuwenden wollen.
Aufgabenstellung
Es handelt sich um ein Roll-up Banner in den Maßen 1m Breite und 2 Meter Höhe.
Das Banner sollte so angelegt sein, dass es interessierten Besuchern auf Kongressen vermittelt, was es mit der Seite Heiterkompass.de auf sich hat. Also wissenschaftlich evaluierte kostenfreie online-Fragebögen, die Menschen dabei helfen Ihre eigenen Stärken und Potenziale zu entdecken und dem eigenen Glück näher zu kommen.
Es sollte außerdem das Logo der NVAS darauf zu sehen sein, sowie kleiner die Logos der Forschungskooperationspartner, HK-Selmhorst, Uni Wolkenrode, Uni Kalbenau, Medical School Trebnitz.
Die Farben sollten zum Logo der NVAS passen.

```html
<!DOCTYPE html>
<html lang="de">
<head>
<meta charset="utf-8">
<title>Roll-Up Heiterkompass</title>
<link rel="stylesheet" href="https://fonts.googleapis.com/css2?family=Fira+Sans:wght@400;500;600;700&display=swap">
<style>
:root{
  --stage:#a9b0bd;
  --navy:#1d3b6a;
  --navy-deep:#0f2a5c;
  --green:#62ab5a;
  --teal:#2aa3bb;
  --white:#ffffff;
  --paper:#e6e8ec;
  --step-1:#6fc1d6;
  --step-2:#239a8e;
  --step-3:#2a9466;
  --step-4:#1f3f73;
}
*{margin:0;padding:0;box-sizing:border-box}
html,body{width:768px;height:1200px;overflow:hidden;background:var(--stage)}
body{font-family:"Fira Sans",sans-serif}
.banner{position:absolute;left:78px;top:0;width:612px;height:1200px;display:flex;flex-direction:column}
.header{height:108px;background:linear-gradient(90deg,var(--green),var(--teal));display:flex;align-items:center;justify-content:center}
.header-url{color:var(--white);font-weight:700;font-size:34px;letter-spacing:-0.5px}
.hero{position:relative;height:343px;overflow:hidden;background:#f4f4f5}
.hero-photo{position:absolute;inset:0;background:linear-gradient(90deg,#f5f5f6 0%,#f1eeea 35%,#d8b08a 58%,#b07a56 72%,#4a4a4c 88%,#2f3136 100%)}
.hero-fade{position:absolute;inset:0;background:linear-gradient(90deg,rgba(255,255,255,.95) 0%,rgba(255,255,255,.7) 40%,rgba(255,255,255,0) 62%)}
.org-mark{position:absolute;left:46px;top:96px;color:var(--navy)}
.org-name{display:flex;align-items:center;gap:8px;font-weight:600;font-size:22px;letter-spacing:1px}
.org-dot{width:14px;height:14px;border-radius:50%;background:var(--teal)}
.org-sub{font-size:9.5px;font-weight:500;line-height:13px;margin-top:4px;width:150px}
.headline{position:absolute;left:43px;top:208px;width:290px;text-align:center;color:var(--navy);font-weight:600;font-size:34px;line-height:48px;letter-spacing:-0.6px}
.info{position:relative;height:595px;background:linear-gradient(20deg,var(--green) 0%,#3fa28c 45%,var(--teal) 100%);color:var(--white)}
.intro{position:absolute;left:45px;top:36px;width:530px;font-size:17px;line-height:23px;font-weight:400}
.steps{position:absolute;left:0;top:0;width:100%;height:100%}
.step-line{position:absolute;left:58px;top:190px;width:2px;height:236px;background:rgba(255,255,255,.7)}
.step-dot{position:absolute;left:45px;width:28px;height:28px;border-radius:50%;border:2px solid var(--white)}
.step-title{position:absolute;left:105px;font-size:23px;font-weight:400;white-space:nowrap}
.step-sub{position:absolute;left:105px;font-size:17px;white-space:nowrap}
.badge{position:absolute;left:432px;top:256px;width:182px;height:56px;background:var(--navy-deep);transform:rotate(-2deg);color:var(--white);font-size:13.5px;line-height:17px;text-align:center;padding-top:10px}
.rule{height:6px;background:var(--navy-deep)}
.partners{position:relative;height:148px;background:var(--paper);color:var(--navy)}
.partners-title{position:absolute;left:45px;top:22px;font-size:18px}
.partner-row{position:absolute;left:45px;right:45px;top:78px;display:flex;justify-content:space-between;align-items:center}
.partner{font-size:11px;font-weight:500;color:var(--navy);white-space:nowrap}
</style>
</head>
<body>
<main class="banner">
  <header class="header"><span class="header-url">www.heiterkompass.de</span></header>

  <section class="hero">
    <div class="hero-photo" role="img" aria-label="Foto eines lachenden jungen Mannes mit Brille vor unscharfem Hintergrund"></div>
    <div class="hero-fade"></div>
    <div class="org-mark">
      <div class="org-name"><span class="org-dot"></span>NVAS</div>
      <div class="org-sub">Nordische Vereinigung für Angewandte Seelenkunde</div>
    </div>
    <h1 class="headline">Kennen Sie sich und Ihre Stärken?</h1>
  </section>

  <section class="info">
    <p class="intro">Unter www.heiterkompass.de haben Sie die Möglichkeit kostenfrei die neusten wissenschaftlichen Fragebögen im Bereich der Positiven Psychologie zu nutzen und ein detailliertes Feedback zu Ihren Ergebnissen zu erhalten.</p>
    <div class="steps">
      <div class="step-line"></div>
      <div class="step-dot" style="top:176px;background:var(--step-1)"></div>
      <div class="step-title" style="top:161px">Online registrieren</div>
      <div class="step-sub" style="top:200px">– und damit immer Zugriff auf Ihre Ergebnisse haben</div>

      <div class="step-dot" style="top:263px;background:var(--step-2)"></div>
      <div class="step-title" style="top:249px">Online-Fragebogen ausfüllen</div>
      <div class="step-sub" style="top:290px">unter www.heiterkompass.de</div>
      <div class="badge">wissenschaftlich evaluiert<br>kostenfrei | anonym</div>

      <div class="step-dot" style="top:353px;background:var(--step-3)"></div>
      <div class="step-title" style="top:339px">Persönliche Rückmeldung erhalten</div>

      <div class="step-dot" style="top:412px;background:var(--step-4)"></div>
      <div class="step-title" style="top:398px">Ein noch erfüllteres Leben gestalten</div>
      <div class="step-sub" style="top:427px">– mit unseren Hinweisen</div>
    </div>
  </section>

  <div class="rule"></div>

  <footer class="partners">
    <h2 class="partners-title" style="font-weight:400">Forschungskooperationspartner</h2>
    <div class="partner-row">
      <span class="partner">Uni Wolkenrode</span>
      <span class="partner">Medical School Trebnitz</span>
      <span class="partner">HK-Selmhorst</span>
      <span class="partner">Uni Kalbenau</span>
    </div>
  </footer>
</main>
</body>
</html>
```